Client Publishing Agency Brochure

We need a company brochure for a new company based in Cape Town, South Africa called Willowmere Lantern Studio (WLS).

We need a brochure marketing our publishing agency (wls:scribe) and our creative, interactive & print production division (wls:forge). Develop a fresh design concept which will direct the design of our new website in the near future. (So don't pay attention to our current web page. It does not reflect our brand).

wls:scribe is a content marketing agency offering our clients (B2B, B2C, NPO, Professional & Membership Organizations) branded publishing to build trust, authority and relationships with their customers. A typical content strategy may include communication through client print or online magazine, newsletters, microsite, website, social technology and plenty more). We want to communicate that company's need to change their mind set from promoting their products and begin to invest in developing a relationship with their potential & existing customers. The drive is a Return On Objectives (business & marketing objectives) and interest is a Return On Investment (ROI).

wls:forge is a creative, interactive & print production agency which supports our client's marketing collateral needs.
Updates

Hi Designers,

This is a response to questions posted earlier to assist you in your project.

Q.What will the size of brochure be?
A. A4 size with folder flap for the back cover

Q.Will it be a three panels double sided?
A. Depends on your creative concept. But if you make a 3 panel dbl side then layout two version for print (double sided 3 panel) and digital pdf (single pdf pages in sequence).

Q.The images that you supplied I know are just samples, What type of images are 
required? 
A. Depends on your creative concept. Let the style of the logo inspire you. What I liked in the examples is the classic, premium, quality feel. So no business stock imagery. I'm also a creative agency so that message needs to come through. Illustrated styles are welcome.

Q.Should design have same feel as your website? 
A. No. Our website is pending the outcome of the brochure. The brochure will be our creative direction for our new website. So creative an inspiring and clean brochure.

Please feel free to post additional questions. Good Luck and thank you for your participation.

Reason: The designers have not produced a style and concept that reflects our brand. Would like to guide them more to reach the right look for our company.

Hi Designers...

I have not been happy with the quality of ideas and execution of those ideas. This I understand could a combination of a poor brief and a non-guarenteed project.

I have rectified the brief and have guaranteed the award. Please don't hold back on your creativity and return the guarantee for high quality.

Please ask me any questions to better understand what we are looking for.

Remember. This brochure is a new design concept. Do not visit the web page for inspiration. The new design concept for the brochure will set the tone and inspire a new website.

Lets create a beautiful product together.

Thank you for your participation.

Reason: Designers are not following the brief, and not respecting the logo and colour policies/guidelines and those who are submitting work are not asking questions throughout the process to get a better understanding of what we need. All design submissions are always at the last minute. And some designers are are not real designers and using web development software to produce print designs. More importantly after taking time to advise designers of changes, no effort is made by designers to make changes. Each designer submits 1 idea and think that they are going to win the lottery. Where is the work ethic and quality of service? Where are the submissions from the designers who accepted the participation fee? There were a few designers who promised participation and never showed up. Maybe it all our fault? But we not happy with the service and level of creativity. Not sure if these designers are taking pride in their work or not. I know a few of you are.

Target Market(s)

B2B, B2C, NPO, Professional & Membership Organizations - Make up professionals and decision makers across sectors from Shipping and Logistics, Manufacturing, Legal to Art & Culture.

Industry/Entity Type

Communication

Requirements
Must have
• Size: A4
x 2 Panels
+ Folder flap (for A4 Paper, business card slot)
Styled map to our premises. See map attachment for example.

Pages: 10 including cover (if you need more than this let your design motivate the need for more pages)

(See logo use eps file)
(See colour use eps file)

Nice to have
• Styled map to our premises. See attachment for example.
Should not have
• Do not take any inspiration from our website. It is just a free template to show customers that it is still under construction.

Do not include stock symbols and typical business stock images. Remember we are a creative offering, so our brochure should show originality, innovation and individuality.

```html
<!DOCTYPE html>
<html lang="en">
<head>
<meta charset="utf-8">
<title>Willowmere Lantern Studio – Brochure Spreads</title>
<link href="https://fonts.googleapis.com/css2?family=Arimo:wght@400;700&display=swap" rel="stylesheet">
<style>
  :root{
    --page:#ffffff;
    --ink:#1a1a1a;
    --muted:#333333;
    --edge:#d6d6d6;
    --brand-red:#d8262e;
    --magenta:#e0218a;
    --panel-grey:rgba(150,150,150,0.72);
    --black:#000000;
    --night:#17061f;
  }
  *{box-sizing:border-box;margin:0;padding:0}
  html,body{width:1200px;height:900px;overflow:hidden;background:#ffffff}
  body{position:relative;font-family:"Arimo",Arial,sans-serif;color:var(--ink)}
  .spread{position:absolute;background:var(--page);border:1px solid var(--edge)}
  .spread--inside{left:237px;top:430px;width:945px;height:442px}
  .spread--outside{left:20px;top:30px;width:1146px;height:516px;z-index:2}

  /* outside: project panel */
  .project{position:absolute;left:0;top:0;width:365px;height:100%;padding:18px 16px 0 58px}
  .icon-tile{position:absolute;width:30px;height:30px;border-radius:7px}
  .project .icon-tile{left:20px;top:20px;background:linear-gradient(135deg,#f5c400,#e8402a 55%,#3aa0d8)}
  .project h2{font-size:11px;font-weight:700;margin-bottom:5px}
  .project p{font-size:6.2px;line-height:8.3px;margin-bottom:3px;color:var(--muted)}
  .project b{font-weight:700}
  .partner{margin-top:10px;font-size:11px;font-weight:700;color:var(--brand-red);display:flex;align-items:center;gap:6px}
  .partner .mark{width:12px;height:12px;background:var(--brand-red)}

  /* outside: cover */
  .cover{position:absolute;left:365px;top:0;width:781px;height:100%;overflow:hidden;
    background:
      radial-gradient(ellipse 260px 200px at 54% 44%,rgba(240,255,230,.95),rgba(150,220,120,.6) 35%,transparent 70%),
      radial-gradient(ellipse 300px 140px at 40% 10%,rgba(120,70,170,.8),transparent 70%),
      radial-gradient(ellipse 220px 180px at 70% 60%,rgba(90,170,210,.55),transparent 70%),
      linear-gradient(180deg,#2c1440 0%,#1a0a26 45%,#2a2a30 100%)}
  .colour-arc{position:absolute;left:545px;top:110px;width:420px;height:406px;border-radius:50%;
    background:radial-gradient(circle at 50% 50%,transparent 0 44%,rgba(0,0,0,0) 44%),
      conic-gradient(from 200deg,#8a3fa0,#3b7bd0,#e0218a,#f28c1a,#f5d20a,#7cc242,#3bb3c9,#8a3fa0)}
  .colour-arc::after{content:"";position:absolute;inset:70px 90px 70px 70px;border-radius:50%;
    background:radial-gradient(circle,rgba(220,230,240,.9),rgba(60,60,80,.95))}
  .find-us{position:absolute;left:52px;top:267px;width:303px;height:229px;background:var(--panel-grey);
    text-align:center;color:#111;padding-top:118px}
  .map{position:absolute;left:68px;top:15px;width:116px;height:88px;border:6px solid #555;
    background:linear-gradient(135deg,#d9d9d9,#b8b8b8)}
  .find-us p{font-size:6.4px;line-height:9.6px}
  .find-us .label{font-weight:700}
  .brand-card{position:absolute;left:465px;top:340px;width:231px;height:96px;background:var(--page);
    display:flex;align-items:center;gap:12px;padding:0 5px 0 10px}
  .brand-card .name{font-size:11px;font-weight:700;color:var(--ink);width:100px;line-height:13px}
  .brand-card .square{width:104px;height:84px;background:var(--black)}

  /* inside */
  .col{position:absolute;top:0}
  .col--left{left:20px;width:300px}
  .col--mid{left:334px;width:292px}
  .section{position:relative;padding-left:0}
  .section h3{font-size:9px;font-weight:700;padding-left:28px;height:16px;line-height:18px;margin-bottom:3px}
  .section .icon-tile{left:0;top:0;width:22px;height:22px;border-radius:5px}
  .section p,.section li{font-size:5.9px;line-height:7.6px;color:var(--muted);margin-bottom:3.5px}
  .section ol{padding-left:10px}
  .tile-a{background:linear-gradient(135deg,#f5d20a,#e0218a)}
  .tile-b{background:linear-gradient(135deg,#3bb3c9,#8a3fa0)}
  .tile-c{background:linear-gradient(135deg,#7cc242,#3b7bd0)}
  .tile-d{background:linear-gradient(135deg,#f28c1a,#d8262e)}
  .flap{position:absolute;left:628px;top:148px;width:317px;height:294px;border-radius:160px 160px 0 0;overflow:hidden;
    background:radial-gradient(circle at 52% 100%,#050505 0 52%,transparent 53%),
      conic-gradient(from 250deg at 52% 100%,#8a3fa0,#3b7bd0,#e0218a,#f28c1a,#f5d20a,#7cc242,#3bb3c9,#8a3fa0)}
  .flap-label{position:absolute;font-size:7px;font-weight:700;color:var(--magenta)}
  .flap-label--cutout{left:663px;top:264px}
  .card-slot{position:absolute;left:778px;top:335px;width:136px;height:86px;background:var(--page);
    display:flex;align-items:center;justify-content:center}
</style>
</head>
<body>

<section class="spread spread--inside">
  <div class="col col--left" style="top:112px">
    <div class="section">
      <span class="icon-tile tile-a" role="img" aria-label="Section icon"></span>
      <h3>Our Approach</h3>
      <p>Shouting out your brand virtues is the old marketer's approach. This type of communication uses marketing collateral (brochures, event marketing material, advertising). Customers care less about how special you are and care more for the relevant difference you make in their lives and business.</p>
      <p>Finding a single opportunity of making a difference is only achieved through consistent meaningful conversations about the interests, issues, and opportunities that matter the most to your audience. It's the art of conversation and engagement versus talking to your valued clients. This type of communication is achieved through content marketing strategies (client magazine, e-zines, newsletters, microsite, website, social technology and plenty more).</p>
      <p>We create lint editorial that sparks conversations within in your community and continuously connect to motivate them to share your strategic message with their extended networks.</p>
      <p>When you begin understanding your clients, whether they are internal (employees) or external, you'll find an opportunity for your brand to be reinforced as a trusted partner. Trust currency your brand should be investing in. Return on Objectives should be your primary success indicator followed by sales. Sustainable relationships will deliver Return on Investment shared with your customers.</p>
      <p>We deliver well-crafted editorial and web content at the point where traditional marketing collateral strategy meets new aged content engineering. It's about bringing real value to your readers while maximizing your marketing and business objectives effectively.</p>
    </div>
    <div class="section" style="margin-top:4px">
      <span class="icon-tile tile-b" role="img" aria-label="Section icon"></span>
      <h3>Client magazines</h3>
      <p>Client magazines are measurably more effective than traditional marketing channels at simultaneously building brand awareness, driving sales and generating loyalty through meaningful engagement.</p>
      <p>We combine our team's journalistic expertise and providing design ideas with subject specialists in your industry to produce content that interests, informs and educates your audience. As a result your branded magazine offers authentic value to readers, achieves ROO, and illuminates your brand colours in your market.</p>
      <p>Our commercial services offer an opportunity of leveraging off advertising and sponsorship, considerably reducing project costs while helping your business audience increase marketing effectiveness.</p>
    </div>
  </div>

  <div class="col col--mid" style="top:112px">
    <div class="section">
      <p>Our team produces the highest quality content on print and digital media and adopts the professional values subscribed to by your organization.</p>
      <p>Our commercial services offer an opportunity of leveraging off advertising and sponsorship, considerably reducing project costs while helping your business audience increase marketing effectiveness.</p>
    </div>
    <div class="section" style="margin-top:4px">
      <span class="icon-tile tile-c" role="img" aria-label="Section icon"></span>
      <h3>Digital solutions</h3>
      <p>Three separate research sources reveal more than 50% of magazine readers want digital content but not at the expense of print.</p>
      <p>Sources:</p>
      <ol>
        <li>Folio Reader Group, 2010, finds amoung current subscribers, 53% chose to renew with a digital product.</li>
        <li>Marketing Leaders Forum, 2010, finds 87% of those interested in reading magazines on a digital device still want a printed copy.</li>
        <li>Larkspur Research, 2010, finds 75% of consumers feel that digital content complements print, yet 25% feel it replaces print.</li>
      </ol>
      <p>Therefore our digital approach is creating creative, engaging and cost-effective scalable compliments to print through HTML, PDF, or microsites.</p>
      <p>Organic SEO principals drive our content engineering style ensuring online visibility, experience and tracking capabilities while your e-publication promotes contagious interactive engagement through a host of features. Features include personalization, graphic artistry, video and rich media, analytics and social media linkage. The result is an interactive communication campaign limitless in engagement capacity in any media wherever your audience might be.</p>
    </div>
    <div class="section" style="margin-top:4px">
      <span class="icon-tile tile-d" role="img" aria-label="Section icon"></span>
      <h3>Marketing collateral</h3>
      <p>Marketing collateral tools are vital to a complete communication campaign and its effectiveness resides in quality editorial content. We can help you improve the way you communicate through your online and print collateral, which may include corporate brochures, management briefings, event support materials, advertising, and anything else you might need to increase effectiveness.</p>
      <p>We provide creative ideas and copy, production &amp; collateral management, commercial printing (press, digital, litho), and delivery of the finished product, whether in print or digital media.</p>
      <p>The result is marketing collateral with a distinct identity and unique strategic message crafted in a language your audience understands.</p>
    </div>
  </div>

  <div class="flap" role="img" aria-label="Folder flap artwork: black dome ringed with colourful rounded squares"></div>
  <span class="flap-label flap-label--cutout">Cutout</span>
  <div class="card-slot"><span class="flap-label" style="position:static">Business Card</span></div>
</section>

<section class="spread spread--outside">
  <div class="project">
    <span class="icon-tile" role="img" aria-label="Active project icon"></span>
    <h2>Active Project</h2>
    <p><b>Client:</b> Port of Kestrel Bay</p>
    <p><b>Project:</b> Port Magazine &amp; Directory</p>
    <p><b>Objective:</b> Thought Leadership and Trust 2011 Content Media: Print, E-zine</p>
    <p><b>Frequency:</b> Annual</p>
    <p><b>2012 Content Pipeline:</b> Print Magazine, E-zine, Newsletter, Microsite</p>
    <p><b>A Few Supporters:</b> Coastal Safety Council, Freight Movers Guild, Southern Trade Chamber, Halden Lift Works, Brightfuel, Norvane Oil, and plenty more.</p>
    <p>WLS Publishing, in collaboration with the Meridian Harbour Authority, is to produce the Port of Kestrel Bay's official annual publication. The Harbour Line magazine, which is set to increase in scope and effectiveness annually, is a valuable resource for thousands of local and international industry professionals. The magazine promotes ports and their region as a port of call for international markets through comprehensively researched editorial and quality photography. This magazine is essential in recognizing the importance of Kestrel Bay's success as a rapidly expanding and efficient logistics hub for commerce and shipping, a city that offers high-standard service and technical expertise in co-operation with business, industry and government. This flagship marketing tool will receive the widest distribution across industrial and shipping industries, both domestically and internationally, and will provide participating organizations with a valuable opportunity to promote and advertise their own expertise and interests.</p>
    <p>Advertising Enquiries: portcity@willowmerelantern.example</p>
    <p>Talk to us about developing your own publication: thandi@willowmerelantern.example</p>
    <div class="partner"><span class="mark"></span>Meridian</div>
  </div>

  <div class="cover" role="img" aria-label="Cover artwork: glowing grid of rounded light squares on deep purple">
    <div class="colour-arc" role="img" aria-label="Arc of colourful rounded squares"></div>
    <div class="find-us">
      <div class="map" role="img" aria-label="Styled street map to the studio premises"></div>
      <p class="label">Find Us:</p>
      <p>Cnr. 3rd Lane &amp; Quarry Road, Brackenfield, Cape Town, 7400, South Africa</p>
      <p class="label">New business enquiries, please contact:</p>
      <p class="label">Thandi Orlov</p>
      <p>t: +27 (0) 21 555 0142 &nbsp;f: +27 (0) 21 555 0143 &nbsp;m: +27 (0) 71 555 0199</p>
      <p>e: thandi@willowmerelantern.example</p>
      <p class="label">Follow Us:</p>
      <p>w: www.willowmerelantern.example</p>
      <p>Read: read.willowmerelantern.example</p>
    </div>
    <div class="brand-card">
      <span class="name">Willowmere Lantern Studio</span>
      <span class="square"></span>
    </div>
  </div>
</section>

</body>
</html>
```